Website Design for Architecture Practice

I need a home page and one sidebar/content page for an Architecture practice delivered in PSD.

This archictecture practice specialises in one-off, high end homes and commercial properties (restaurant) heavily influenced by Dorian Vessey Kent, particularly his work on the Tarrowby Museum

I am looking for a home page, and a generic content page where we can outline our services, and showcase our homes.

http://notes.qorvenuni.edu.au/studio/Tarrowby%20Lisdane%202.jpg

Target Market(s)

30-70yr old (typically wealthy) property buyers, developers and investors

Industry/Entity Type

Architecture

Number of Pages Required

2 page

Font styles to use
Serif
Sans Serif

Requirements
Must have
• Home page design
• a Content Page design (ie, top nav with sidebar)
Nice to have
• Use any Dorian Vessey Kent images you can find via google etc as placeholders for our own photography (ie they don't need to be licensed as we will be replacing with our own commissioned photography). Full color preferred but feel free to experiment with treating any images as you see fit.

```html
<!DOCTYPE html>
<html lang="en">
<head>
<meta charset="utf-8">
<title>Vessmark Studio</title>
<link rel="stylesheet" href="https://fonts.googleapis.com/css2?family=Open+Sans:wght@400;600;700&family=Raleway:wght@300;400;600&display=swap">
<style>
:root{
  --blue:#4fa3dc;
  --blue-soft:#6cb8e4;
  --blue-pale:#e3f1fb;
  --ink:#4a4a4a;
  --muted:#7a7a7a;
  --line:#dcdcdc;
  --grey-band:#f1f1f1;
  --strip:#e6e6e6;
  --footer:#0e0e0e;
  --white:#ffffff;
}
*{margin:0;padding:0;box-sizing:border-box}
html,body{width:702px;height:1200px;overflow:hidden;background:var(--white)}
body{font-family:"Open Sans",Arial,sans-serif;color:var(--ink);position:relative}
.page{position:relative;width:702px;height:1200px;overflow:hidden}

/* header */
.site-header{position:absolute;top:0;left:0;width:702px;height:50px;background:var(--white);z-index:3;border-bottom:1px solid var(--line)}
.brand{position:absolute;left:20px;top:0;width:124px;height:60px;background:var(--white);border-radius:0 0 10px 10px;z-index:4;display:flex;align-items:center;justify-content:center;box-shadow:0 2px 4px rgba(0,0,0,.15)}
.brand-name{font-family:"Raleway",sans-serif;font-weight:600;color:var(--ink);font-size:13px;line-height:16px;text-align:center;letter-spacing:.3px}
.main-nav{position:absolute;left:196px;top:15px;display:flex;gap:4px}
.main-nav a{display:block;font-size:8px;font-weight:600;color:var(--ink);text-decoration:none;text-transform:uppercase;padding:5px 10px;letter-spacing:.3px}
.main-nav a.is-active{background:var(--blue-pale);border:1px solid #bcdcf2;color:var(--blue)}
.social{position:absolute;right:22px;top:15px;display:flex;gap:8px}
.social span{width:17px;height:17px;border:1px solid #9a9a9a;border-radius:50%;display:block}

/* hero */
.hero{position:absolute;top:50px;left:0;width:702px;height:301px;background:linear-gradient(180deg,#6f8fae 0%,#a9b9c8 45%,#d9dde0 70%,#7a8a7a 100%)}
.hero-title{position:absolute;top:168px;left:0;width:100%;text-align:center;font-family:"Raleway",sans-serif;font-weight:400;color:var(--white);font-size:31px;line-height:36px;text-transform:uppercase;letter-spacing:.5px;text-shadow:0 1px 3px rgba(0,0,0,.3)}
.btn{display:inline-block;background:var(--blue);color:var(--white);font-size:7.5px;font-weight:600;text-transform:uppercase;padding:5px 13px;border-radius:2px;letter-spacing:.3px}
.hero .btn{position:absolute;top:253px;left:50%;transform:translateX(-50%)}

/* thumbnail strip */
.strip{position:absolute;top:351px;left:0;width:702px;height:59px;background:var(--strip);display:flex;align-items:center;justify-content:center;gap:7px}
.strip .thumb{width:80px;height:46px;background:linear-gradient(160deg,#b7c6d4,#8d9a8c)}
.strip .arrow{width:18px;height:18px;border-radius:50%;background:var(--white);display:flex;align-items:center;justify-content:center;margin:0 18px}

/* welcome + news */
.intro{position:absolute;top:436px;left:28px;width:348px}
.section-title{font-family:"Raleway",sans-serif;font-weight:400;color:var(--blue);font-size:22px;line-height:26px}
.intro p{margin-top:12px;font-size:8.5px;line-height:15.5px;color:var(--muted);text-align:justify}
.intro .btn{margin-top:14px}
.news{position:absolute;top:436px;left:398px;width:282px}
.news-head{display:flex;justify-content:space-between;align-items:baseline}
.news-head a{font-size:7px;color:var(--blue);text-decoration:none}
.news-list{list-style:none;margin-top:10px}
.news-item{display:flex;gap:10px;padding:7px 0;border-bottom:1px solid #eee}
.news-item .thumb{flex:0 0 56px;height:44px;background:linear-gradient(170deg,#aebdcb,#7f8b7a)}
.news-date{font-size:6.5px;color:#9a9a9a}
.news-item h3{font-size:10px;font-weight:600;color:var(--ink);margin:1px 0 2px}
.news-item p{font-size:7px;line-height:11px;color:var(--muted)}

/* services */
.services{position:absolute;top:667px;left:0;width:702px;height:281px;background:var(--grey-band)}
.services .section-title{text-align:center;margin-top:30px}
.service-grid{display:flex;gap:13px;padding:0 28px;margin-top:14px}
.service{width:203px}
.service .photo{height:112px}
.service h3{margin-top:10px;font-size:8px;font-weight:700;color:var(--blue);text-transform:uppercase}
.service p{font-size:7px;line-height:11px;color:var(--muted);margin-top:3px;height:22px;overflow:hidden}
.service .btn{margin-top:8px;background:var(--white);color:var(--muted);border:1px solid var(--line)}

/* newsletter */
.newsletter{position:absolute;top:948px;left:0;width:702px;height:175px;background:var(--blue-soft);text-align:center;color:var(--white)}
.newsletter h2{font-family:"Raleway",sans-serif;font-weight:400;font-size:24px;margin-top:34px}
.subscribe{display:flex;justify-content:center;margin-top:18px}
.subscribe .field{width:196px;height:40px;background:var(--white);color:#888;font-size:9px;text-align:left;padding:13px 12px;border-radius:2px 0 0 2px}
.subscribe .submit{width:118px;height:40px;background:#0c0c0c;color:var(--white);font-size:16px;line-height:40px;margin-left:12px;border-radius:2px}
.newsletter p{font-size:7.5px;line-height:12px;width:250px;margin:12px auto 0;color:#eef7fd}

/* footer */
.site-footer{position:absolute;top:1123px;left:0;width:702px;height:77px;background:var(--footer);text-align:center;color:var(--white)}
.footer-nav{font-size:8px;margin-top:25px;word-spacing:1px}
.copyright{font-size:6.5px;color:#6e6e6e;margin-top:6px}
.footer-social{position:absolute;right:28px;top:25px;display:flex;gap:11px}
.footer-social span{width:9px;height:9px;border-radius:50%;background:var(--blue)}
</style>
</head>
<body>
<div class="page">

  <header class="site-header">
    <nav class="main-nav">
      <a href="#" class="is-active">Home</a>
      <a href="#">About Us</a>
      <a href="#">Our Services</a>
      <a href="#">Testimonials</a>
      <a href="#">Gallery</a>
      <a href="#">Contact</a>
    </nav>
    <div class="social"><span></span><span></span><span></span></div>
  </header>
  <div class="brand"><div class="brand-name">Vessmark<br>Studio</div></div>

  <section class="hero" role="img" aria-label="Photograph of a white curved modern house with large glazed openings">
    <h1 class="hero-title">Professional Architecture<br>Solutions</h1>
    <span class="btn">Read More</span>
  </section>

  <div class="strip">
    <span class="arrow"><svg width="6" height="8" viewBox="0 0 6 8"><path d="M5 0L1 4l4 4" fill="none" stroke="#777" stroke-width="1.4"/></svg></span>
    <div class="thumb" role="img" aria-label="Thumbnail of a modern house"></div>
    <div class="thumb" role="img" aria-label="Thumbnail of a patterned facade"></div>
    <div class="thumb" role="img" aria-label="Thumbnail of a residence at dusk"></div>
    <div class="thumb" role="img" aria-label="Thumbnail of a brick building"></div>
    <div class="thumb" role="img" aria-label="Thumbnail of a sculptural building"></div>
    <span class="arrow"><svg width="6" height="8" viewBox="0 0 6 8"><path d="M1 0l4 4-4 4" fill="none" stroke="#777" stroke-width="1.4"/></svg></span>
  </div>

  <section class="intro">
    <h2 class="section-title">Welcome to Architecture Practice</h2>
    <p>We design one-off homes and commercial spaces shaped by light, landscape and the people who use them. Each project begins with a careful study of the site and ends with a building that feels inevitable in its place. Our studio works closely with clients, builders and engineers from first sketch to final handover, keeping every detail honest and every line deliberate. From coastal residences to intimate restaurants, we bring the same patience and craft to every commission, large or small. Curved walls, deep openings and quiet materials define our work.</p>
    <span class="btn">Read More</span>
  </section>

  <section class="news">
    <div class="news-head"><h2 class="section-title">Latest News</h2><a href="#">View All</a></div>
    <ul class="news-list">
      <li class="news-item">
        <div class="thumb" role="img" aria-label="Photo of a contemporary home"></div>
        <div><div class="news-date">Posted 12 March</div><h3>Lorem Ipsum Dolor Sit</h3><p>Our hillside residence is shortlisted for a regional design award.</p></div>
      </li>
      <li class="news-item">
        <div class="thumb" role="img" aria-label="Photo of a restaurant building"></div>
        <div><div class="news-date">Posted 04 March</div><h3>Lorem Ipsum Dolor Sit</h3><p>A new restaurant interior opens on the harbour this spring.</p></div>
      </li>
      <li class="news-item">
        <div class="thumb" role="img" aria-label="Photo of a family house"></div>
        <div><div class="news-date">Posted 21 February</div><h3>Lorem Ipsum Dolor Sit</h3><p>Studio tours return with guided walks through recent homes.</p></div>
      </li>
    </ul>
  </section>

  <section class="services">
    <h2 class="section-title">Our Service</h2>
    <div class="service-grid">
      <article class="service">
        <div class="photo" role="img" aria-label="Photo of hands working on architectural plans" style="background:linear-gradient(150deg,#d9dde2,#9fb1c4)"></div>
        <h3>Consectetur Adipiscing Elit</h3>
        <p>Concept design and planning for bespoke private homes built to last.</p>
        <span class="btn">Read More</span>
      </article>
      <article class="service">
        <div class="photo" role="img" aria-label="Photo of a building under construction" style="background:linear-gradient(160deg,#8aa0b0,#5b6b58)"></div>
        <h3>Consectetur Adipiscing Elit</h3>
        <p>Restaurant and retail interiors with a strong sense of place.</p>
        <span class="btn">Read More</span>
      </article>
      <article class="service">
        <div class="photo" role="img" aria-label="Photo of colourful material samples" style="background:linear-gradient(90deg,#d9a441,#c85c5c,#6f9fd0,#7cbf8a)"></div>
        <h3>Consectetur Adipiscing Elit</h3>
        <p>Material studies, models and full drawings for every project.</p>
        <span class="btn">Read More</span>
      </article>
    </div>
  </section>

  <section class="newsletter">
    <h2>Subscribe to Our Newsletter</h2>
    <div class="subscribe">
      <div class="field">Email Address</div>
      <div class="submit">Subscribe</div>
    </div>
    <p>Receive project news, studio events and design notes from our team, delivered once a month to your inbox.</p>
  </section>

  <footer class="site-footer">
    <div class="footer-nav">Home | About Us | Our Services | Testimonials | Gallery | Contact</div>
    <div class="copyright">Copyright 2024 Vessmark Studio. All rights reserved.</div>
    <div class="footer-social"><span></span><span></span><span></span><span></span><span></span></div>
  </footer>

</div>
</body>
</html>
```